A layout of a webpage for oil trade platform

I would like to have a desgin of one page webpage (with section scrollling dowin) that woulf present the new product i.e. oil trade platform for wholesale buyers and sellers.
Layout should consist of the sections similar to the given at: https://klinika.pewnywybor.pl/system-zarzadzania-wizytami
However oil industy require more colors and more photo stories than here for doctor.
I. I woul imagine at first below menu a slider with brueg information about the product and its advantages with "more" button next to the prict screen of our platform on different displays (PC and mobile).
II. Bellow the slider I would imagine icons correspoing to the advantages of that plaftorm:
1. Purchase/sale process automation 24/7
2. Access to the best deals
3. Electronic offerings and orderings
4. Transaction status monitoring
5. Data and transaction security
II A) (optional):
In near future we would like to prepare a short video presenation. Hence please prepare a place to display that element here.
At the moment alternatvily please prepare a How it works section that would explan the platform operating process
III. Next secion is about benefits for Oil Purchaser
It can be done either by icons of by text and corresponding grahip for while section.
Benefits:
- Access to cheaper oil
- Convenience of online orders
- Possibility to compare prices on the market
- Transaction history
- Order status monitoring
- Seccurity and transparency of purchase
IV. Next seciont is about benefits for Oil Seller
Benefits:
- New sale channel
- Attracting new clients
- More oil sold
- Transaction security
- Possibility to integrate with distribution infrastructure and logistits for more efficient automation.
V. Contact form
VI. Footer
I would need a layout that that will correspond to the very dynamic logo but I would expect also a clean form, smoth and modern. It has to be proffessional layout with more corporate character.
It can use a paralax features if needed.

```html
<!DOCTYPE html>
<html lang="en">
<head>
<meta charset="utf-8">
<title>Oleandra – Oil Trade Platform</title>
<link rel="stylesheet" href="https://fonts.googleapis.com/css2?family=Raleway:wght@400;500;600;700;800&display=swap">
<style>
  :root {
    --ink: #1b1f2a;
    --navy: #1c2d55;
    --nav-active: #1f4d7a;
    --orange: #d0522a;
    --orange-light: #f2843c;
    --band: #ebebeb;
    --white: #ffffff;
    --panel: rgba(40, 42, 52, 0.78);
  }
  * { box-sizing: border-box; margin: 0; padding: 0; }
  html, body { width: 1200px; height: 1000px; overflow: hidden; background: var(--white); }
  body { font-family: "Raleway", sans-serif; color: var(--ink); position: relative; }

  .site-header { position: absolute; left: 0; top: 0; width: 1200px; height: 116px; background: var(--white); border-bottom: 3px solid #dcdcdc; }
  .brand { position: absolute; left: 58px; top: 38px; display: flex; align-items: center; gap: 12px; }
  .brand-dot { width: 34px; height: 34px; border-radius: 50%; background: var(--navy); }
  .brand-name { font-weight: 800; font-size: 28px; color: var(--navy); letter-spacing: 0.5px; }
  .main-nav { position: absolute; left: 306px; top: 0; height: 95px; display: flex; }
  .main-nav a { display: block; height: 95px; line-height: 122px; padding: 0 20px; font-size: 16px; letter-spacing: 4.4px; color: var(--ink); text-decoration: none; font-weight: 500; }
  .main-nav a.is-active { color: var(--nav-active); font-weight: 700; border-bottom: 2px solid var(--navy); padding: 0 24px 0 29px; }
  .search-icon { position: absolute; left: 1101px; top: 51px; }

  .hero { position: absolute; left: 0; top: 118px; width: 1200px; height: 596px; background: linear-gradient(100deg, #5b5c6e 0%, #6e6a78 35%, #7d7680 55%, #8e8a92 75%, #a9a7ad 100%); }
  .hero-panel { position: absolute; left: 150px; top: 85px; width: 272px; height: 430px; background: var(--panel); }
  .hero-feature { position: absolute; left: 10px; top: 4px; width: 246px; height: 133px; background: var(--orange); color: var(--white); font-weight: 700; }
  .hero-item { position: absolute; left: 0; width: 256px; color: var(--white); font-weight: 500; }
  .hero-feature, .hero-item { display: flex; align-items: center; justify-content: center; text-align: center; font-size: 19px; letter-spacing: 4px; line-height: 33.5px; }
  .hero-rule { position: absolute; left: 10px; width: 246px; height: 2px; background: rgba(255,255,255,0.75); }
  .hero-arrow { position: absolute; top: 280px; }
  .hero-cta { position: absolute; left: 612px; top: 430px; }
  .hero-cta-text { position: absolute; left: 704px; top: 447px; color: var(--white); font-weight: 700; font-size: 17px; letter-spacing: 3.6px; line-height: 33px; }

  .news-band { position: absolute; left: 0; top: 714px; width: 1200px; height: 95px; background: var(--band); }
  .news-icon { position: absolute; left: 154px; top: 23px; }
  .news-title { position: absolute; left: 240px; top: 36px; font-size: 14px; letter-spacing: 2.7px; color: #333; font-weight: 500; }
  .news-date { position: absolute; left: 240px; top: 58px; font-size: 9px; letter-spacing: 2px; font-style: italic; font-weight: 700; color: #333; }
  .news-sound { position: absolute; left: 1054px; top: 28px; }

  .advantages { position: absolute; left: 0; top: 809px; width: 1200px; height: 191px; }
  .advantages-media { position: absolute; left: 0; top: 0; width: 615px; height: 191px; background: linear-gradient(90deg, #d9dcdf 0%, #ececec 40%, #e4e4e6 100%); }
  .advantages-divider { position: absolute; left: 615px; top: 0; width: 4px; height: 191px; background: var(--orange-light); }
  .section-title { position: absolute; left: 55px; top: 96px; font-size: 48px; font-weight: 400; letter-spacing: 11px; color: var(--ink); white-space: nowrap; }
  .section-title .accent { color: var(--orange-light); display: inline-block; padding-left: 6px; border-bottom: 1px solid var(--navy); border-right: 1px solid var(--navy); line-height: 52px; }
</style>
</head>
<body>
  <header class="site-header">
    <div class="brand"><span class="brand-dot"></span><span class="brand-name">OLEANDRA</span></div>
    <nav class="main-nav">
      <a href="#" class="is-active">HOME</a>
      <a href="#">ADVANGE</a>
      <a href="#">PURCHARSER</a>
      <a href="#">SELLER</a>
      <a href="#">CONTACT</a>
    </nav>
    <svg class="search-icon" width="28" height="28" viewBox="0 0 28 28" fill="none" stroke="#f2843c" stroke-width="2"><circle cx="11" cy="11" r="9"/><line x1="17.5" y1="17.5" x2="25" y2="25"/></svg>
  </header>

  <section class="hero" role="img" aria-label="Photo of a driver at a fuel station pump beside a car">
    <div class="hero-panel">
      <div class="hero-feature">THE BEST<br>DEAL ON THE<br>MARKET</div>
      <div class="hero-rule" style="top:140px"></div>
      <div class="hero-item" style="top:148px;height:134px">THE BEST<br>DEAL ON THE<br>MARKET</div>
      <div class="hero-rule" style="top:292px"></div>
      <div class="hero-item" style="top:300px;height:134px">THE BEST<br>DEAL ON THE<br>MARKET</div>
    </div>
    <svg class="hero-arrow" style="left:72px" width="26" height="42" viewBox="0 0 26 42" fill="none" stroke="#e8e8ee" stroke-width="2.5"><polyline points="22,2 4,21 22,40"/></svg>
    <svg class="hero-arrow" style="left:1106px" width="26" height="42" viewBox="0 0 26 42" fill="none" stroke="#e8e8ee" stroke-width="2.5"><polyline points="4,2 22,21 4,40"/></svg>
    <svg class="hero-cta" width="533" height="86" viewBox="0 0 533 86">
      <polygon points="60,0 533,0 470,86 0,86" fill="#1c2d55" fill-opacity="0.85"/>
      <circle cx="429" cy="43" r="25" fill="none" stroke="#fff" stroke-width="2"/>
      <polyline points="424,31 435,43 424,55" fill="none" stroke="#fff" stroke-width="2"/>
    </svg>
    <div class="hero-cta-text">LOREM IPSUM DOLOR<br>SIT AMET MASME TIN</div>
  </section>

  <section class="news-band">
    <svg class="news-icon" width="50" height="50" viewBox="0 0 50 50" fill="none" stroke="#d0522a" stroke-width="2">
      <rect x="10" y="2" width="38" height="44"/><path d="M10 30 H2 V42 a4 4 0 0 0 8 0"/>
      <line x1="16" y1="12" x2="42" y2="12"/><rect x="16" y="18" width="26" height="10"/><line x1="16" y1="34" x2="42" y2="34"/><line x1="16" y1="40" x2="42" y2="40"/>
    </svg>
    <p class="news-title">VIVAMUS IMPERDIET, SUSPENDISSE IMPERDIET NULLA INTEGER LITORA PURUS</p>
    <p class="news-date">13-MAY-17</p>
    <svg class="news-sound" width="34" height="24" viewBox="0 0 34 24" fill="none" stroke="#d0522a" stroke-width="1.8">
      <path d="M2 8 H8 L20 2 V22 L8 16 H2 Z"/><path d="M25 8 q3 4 0 8"/><path d="M29 5 q5 7 0 14"/>
    </svg>
  </section>

  <section class="advantages">
    <div class="advantages-media" role="img" aria-label="Photo of a fuel pump nozzle"></div>
    <div class="advantages-divider"></div>
    <h2 class="section-title">THE <span class="accent">ADVANGE</span></h2>
  </section>
</body>
</html>
```